Business Card Design Project

Use newly designed logo and tie into newly designed website
I need a new logo and website layout designed for my partner's business. This is a birthday present. His business is interior painting, wallpapering and design. He also has access to a wide variety of products including carpet, fabrics, furniture, wallpaper, tile, countertops, etc. I have attached some screen shots of his website for reference. He is a one man shop and has a stellar reputation with his customers. He is on-time, very tidy, excellent with animals, and always finishes on time and on budget. There are no restrictions on colors or fonts. The logo needs to work well with the website, business cards and printed materials. The website needs to flow content for device size so it looks just as good on a cell phone or tablet as it does on a desktop computer. Whatever the heck that's called!Thanks. I am looking forward to seeing everyone's ideas.
Target Market(s)
Consumers looking to improve the interior environment of their homes by updating wall paint or paper, flooring (either carpet, tile, or hardwoods), counter tops, window treatments, etc. Clients tend to be more upper middle class and have certain taste levels and expectations. New logo, website and business card should align to meet those levels.
Industry/Entity Type
Cell Phone
Look and feel

```html
<!DOCTYPE html>
<html lang="en">
<head>
<meta charset="utf-8">
<title>Marvella Interior Designs – Business Card</title>
<link href="https://fonts.googleapis.com/css2?family=Open+Sans:wght@400;700&display=swap" rel="stylesheet">
<style>
  :root {
    --backdrop: #4a4a4a;
    --card-top: #b0662e;
    --card-bottom: #84351f;
    --panel: #f5f7f6;
    --panel-shadow: #4a1e0c;
    --ink: #111111;
    --on-card: #ffffff;
  }
  * { margin: 0; padding: 0; box-sizing: border-box; }
  html, body {
    width: 1200px; height: 999px; overflow: hidden;
    background: var(--backdrop);
    font-family: "Open Sans", sans-serif;
  }
  .card {
    position: absolute; left: 75px; top: 199px;
    width: 1050px; height: 600px;
    background: linear-gradient(to bottom, var(--card-top), var(--card-bottom));
  }
  .brand {
    position: absolute; left: 40px; top: 228px;
    color: var(--on-card); font-weight: 400; line-height: 1;
    display: flex; align-items: center; gap: 22px;
  }
  .brand-mark {
    width: 20px; height: 20px; background: var(--on-card);
  }
  .brand-name { font-size: 68px; }
  .brand-tagline { font-size: 36px; margin-top: 8px; }
  .panel {
    position: absolute; left: 583px; width: 467px; height: 134px;
    background: var(--panel);
    box-shadow: -4px 4px 0 var(--panel-shadow);
    color: var(--ink);
  }
  .panel--identity { top: 78px; }
  .panel--contact { top: 244px; }
  .panel--address { top: 409px; }
  .person-title {
    position: absolute; left: 39px; top: 24px;
    font-size: 38px; font-weight: 700; line-height: 1.2;
  }
  .person-role {
    position: absolute; left: 44px; top: 74px;
    font-size: 25px; line-height: 1.2;
  }
  .contact-list { list-style: none; position: absolute; left: 37px; top: 12px; }
  .contact-item {
    display: flex; align-items: center; gap: 18px;
    font-size: 25px; line-height: 35px;
  }
  .contact-icon { width: 27px; height: 27px; flex: none; }
  .address {
    position: absolute; left: 41px; top: 14px;
    font-style: normal; font-size: 25px; line-height: 35px;
  }
</style>
</head>
<body>
  <section class="card">
    <div class="brand">
      <span class="brand-mark"></span>
      <div>
        <div class="brand-name">Marvella</div>
        <div class="brand-tagline">Interior Designs</div>
      </div>
    </div>

    <div class="panel panel--identity">
      <h1 class="person-title">Title name</h1>
      <p class="person-role">designation</p>
    </div>

    <div class="panel panel--contact">
      <ul class="contact-list">
        <li class="contact-item">
          <svg class="contact-icon" viewBox="0 0 24 24" aria-hidden="true">
            <rect x="3" y="1" width="18" height="22" rx="3" fill="#111"/>
            <rect x="6" y="4" width="12" height="14" fill="#f5f7f6"/>
            <path d="M9 15 L15 7" stroke="#111" stroke-width="1.5"/>
          </svg>
          <span>(555) 214-3380</span>
        </li>
        <li class="contact-item">
          <svg class="contact-icon" viewBox="0 0 24 24" aria-hidden="true">
            <path d="M2 10 L12 2 L22 10 V22 H2 Z" fill="#111"/>
            <path d="M2 10 L12 17 L22 10" fill="none" stroke="#f5f7f6" stroke-width="1.5"/>
            <circle cx="12" cy="10" r="2.5" fill="#f5f7f6"/>
          </svg>
          <span>dane@marvelladesigns.com</span>
        </li>
        <li class="contact-item">
          <svg class="contact-icon" viewBox="0 0 24 24" aria-hidden="true">
            <circle cx="12" cy="12" r="10" fill="none" stroke="#111" stroke-width="2.5"/>
            <ellipse cx="12" cy="12" rx="4" ry="10" fill="none" stroke="#111" stroke-width="2"/>
            <path d="M2 12 H22 M4 7 H20 M4 17 H20" stroke="#111" stroke-width="2"/>
          </svg>
          <span>www.marvelladesigns.com</span>
        </li>
      </ul>
    </div>

    <div class="panel panel--address">
      <address class="address">
        Dane Marvella<br>
        48210 W Birchwood Ct.<br>
        Fairmont, KS 66000
      </address>
    </div>
  </section>
</body>
</html>
```